TK Joinery

Cabinet maker. Kitchens. Wardrobes. Vanitys. Entertainment units

Target Market(s)

Modern contemporary.geometry. colours black, gray, charcoal and orange. Matt card gloss letters

Industry/Entity Type

Entertainment

Contact Information for Business Card

Mattias Velder 0418 295 437
mattias.velder@fernmail.test
ABN 471 9052 8316

Font styles to use
Decorative

Colors
000000

Requirements
Should not have
• Pictures

```html
<!DOCTYPE html>
<html lang="en">
<head>
<meta charset="utf-8">
<title>TK Joinery – Business Card</title>
<link rel="stylesheet" href="https://fonts.googleapis.com/css2?family=Federo&family=Marcellus&display=swap">
<style>
  :root {
    --backdrop: #2a2522;
    --card-black: #080808;
    --card-edge: #1c1c1c;
    --orange: #f2a11f;
    --gray: #8a8a8a;
    --light-gray: #b9b9b9;
  }
  * { margin: 0; padding: 0; box-sizing: border-box; }
  html, body {
    width: 1200px;
    height: 900px;
    overflow: hidden;
    background: var(--backdrop);
  }
  .canvas {
    width: 1200px;
    height: 900px;
    display: flex;
    flex-direction: column;
    align-items: center;
    justify-content: center;
    gap: 40px;
  }
  .card {
    position: relative;
    width: 660px;
    height: 377px;
    background: linear-gradient(135deg, #121212 0%, var(--card-black) 55%, #000 100%);
    border: 1px solid var(--card-edge);
    box-shadow: 0 10px 30px rgba(0,0,0,0.55);
  }

  /* Info side */
  .card-info .name-line {
    position: absolute;
    top: 52px;
    left: 50px;
    display: flex;
    align-items: baseline;
    gap: 12px;
  }
  .person-name {
    font-family: "Federo", sans-serif;
    font-size: 30px;
    letter-spacing: 2px;
    text-transform: uppercase;
    color: var(--orange);
  }
  .person-role {
    font-family: "Marcellus", serif;
    font-size: 12px;
    letter-spacing: 1.5px;
    text-transform: uppercase;
    color: #4a4a4a;
  }
  .service-list {
    position: absolute;
    left: 60px;
    bottom: 50px;
    list-style: none;
    font-family: "Marcellus", serif;
    font-size: 18px;
    line-height: 26px;
    color: var(--light-gray);
  }
  .service-list li {
    display: flex;
    align-items: center;
    gap: 16px;
  }
  .service-list li::before {
    content: "";
    width: 8px;
    height: 8px;
    background: var(--orange);
    transform: rotate(45deg);
  }
  .phone {
    position: absolute;
    right: 50px;
    top: 176px;
    display: flex;
    align-items: center;
    gap: 8px;
    font-family: "Marcellus", serif;
    font-size: 20px;
    letter-spacing: 1px;
    color: var(--orange);
  }
  .phone svg { width: 20px; height: 16px; fill: var(--orange); }

  /* Brand side */
  .card-brand {
    display: flex;
    align-items: center;
    justify-content: center;
  }
  .brand-name {
    font-family: "Federo", sans-serif;
    font-size: 58px;
    letter-spacing: 3px;
    text-transform: uppercase;
    color: var(--orange);
  }
</style>
</head>
<body>
  <main class="canvas">
    <section class="card card-info">
      <div class="name-line">
        <span class="person-name">Mattias Velder</span>
        <span class="person-role">Cabinet Maker</span>
      </div>
      <ul class="service-list">
        <li>Kitchens</li>
        <li>Wardrobes</li>
        <li>Vanitys</li>
        <li>Entertainment units</li>
      </ul>
      <div class="phone">
        <svg viewBox="0 0 20 16" aria-hidden="true">
          <path d="M1 5c0-2 4-4 9-4s9 2 9 4v1.5h-4.5V4.5h-9v2H1z"/>
          <path d="M5 8h10l3 7H2z"/>
        </svg>
        <span>0418 295 437</span>
      </div>
    </section>

    <section class="card card-brand">
      <span class="brand-name">TK Joinery</span>
    </section>
  </main>
</body>
</html>
```